Business Card Design

Very plain simple card, Plain modern font. Background. Grey fading to black. Large Bright lime green text. Saying.

TWR-ZA.COM

Small other details in white text.

Irish Horse Sales . Livery . Stud . Shows

Mark Dabrowski
TWR
Birch Lodge
Carrowmede Lane
Thistlecombe
Lincolnshire
LN4 7JX

Email. Twrzap@mailvale.co.uk
Tel. 07482 936504

Industry/Entity Type

Business

Contact Information for Business Card

As below

```html
<!DOCTYPE html>
<html lang="en">
<head>
<meta charset="utf-8">
<title>TWR-ZA.COM Business Card</title>
<link rel="stylesheet" href="https://fonts.googleapis.com/css2?family=Roboto+Condensed:wght@400;700&display=swap">
<style>
  :root {
    --stage-light: #8a8f8c;
    --stage-dark: #3a3e3d;
    --card-paper: #ffffff;
    --frame-red: #d01417;
    --panel-light: #5d6b6b;
    --panel-mid: #2b3433;
    --panel-dark: #040807;
    --lime: #5fb12c;
    --photo-green: #17803a;
    --photo-dark: #0a3a16;
    --text-white: #ffffff;
    --rule-grey: #c9cfcd;
    --edge-grey: #9aa3a1;
  }
  * { box-sizing: border-box; margin: 0; padding: 0; }
  html, body { width: 1200px; height: 900px; overflow: hidden; }
  body {
    position: relative;
    font-family: "Roboto Condensed", "Arial Narrow", sans-serif;
    background: radial-gradient(ellipse 70% 65% at 50% 45%, var(--stage-light), var(--stage-dark));
  }
  .card {
    position: absolute; left: 86px; top: 113px; width: 1039px; height: 684px;
    background: var(--card-paper);
  }
  .card-frame {
    position: absolute; left: 18px; top: 17px; width: 1002px; height: 647px;
    border: 3px solid var(--frame-red);
  }
  .card-face {
    position: absolute; left: 30px; top: 34px; width: 981px; height: 613px;
    overflow: hidden;
    background: radial-gradient(ellipse 60% 80% at 27% 42%, var(--panel-light) 0%, var(--panel-mid) 48%, var(--panel-dark) 100%);
    border-bottom: 3px solid var(--edge-grey);
  }
  .fruit-photo {
    position: absolute; left: 580px; top: 46px; width: 401px; height: 520px;
    background: linear-gradient(160deg, var(--photo-green), var(--photo-dark));
  }
  .brand-name {
    position: absolute; left: 20px; top: 80px;
    font-weight: 700; font-size: 86px; line-height: 1;
    letter-spacing: 6px; color: var(--lime);
  }
  .brand-rule {
    position: absolute; left: 21px; top: 171px; width: 533px; height: 2px;
    background: var(--rule-grey);
  }
  .services, .address, .contact {
    position: absolute; color: var(--text-white);
    font-size: 28px; letter-spacing: -0.5px;
  }
  .services { left: 28px; top: 193px; }
  .address { left: 28px; top: 272px; list-style: none; line-height: 40px; }
  .contact { font-size: 23px; top: 577px; }
  .contact-tel { left: 23px; font-size: 24px; }
  .contact-email { left: 336px; }
</style>
</head>
<body>
  <div class="card">
    <div class="card-frame"></div>
    <div class="card-face">
      <div class="fruit-photo" role="img" aria-label="Photograph of a green-tinted lime fruit"></div>
      <div class="brand-name">TWR-ZA.COM</div>
      <div class="brand-rule"></div>
      <p class="services">Irish Horse Sales . Livery . Stud . Shows</p>
      <ul class="address">
        <li>Mark Dabrowski</li>
        <li>TWR</li>
        <li>Birch Lodge</li>
        <li>Carrowmede Lane</li>
        <li>Thistlecombe</li>
        <li>Lincolnshire</li>
        <li>LN4 7JX</li>
      </ul>
      <p class="contact contact-tel">Tel. 07482 936504</p>
      <p class="contact contact-email">Email. Twrzap@mailvale.co.uk</p>
    </div>
  </div>
</body>
</html>
```